Professional Single Page Website Design for Vellowind Advisory

Vellowind Advisory is a new business consultancy specializing in providing expert services to small businesses, primarily in the brick-and-mortar retail and food service sectors. We offer a range of services including franchise development and launch, due diligence, and construction management.

Currently, we have a basic website set up at www.vellowindadvisory.example, but we need a professional touch to enhance its design and functionality.

Project Requirements:
- Single Page Design: For now, we need a single page design that effectively showcases who we are, our services, and contact information.
- Future Expansion: The design should be flexible and scalable for future expansion to include additional pages like specific service offerings, about us, and a dedicated contact page.
- Design Aesthetic: We are looking for a modern yet professional design that aligns with our brand identity.
- Logo: We have a logo that we like, which was also sourced from Pixel Forum. The logo files are attached to this project brief.

Key Sections to Include:
- Hero Section: An engaging introduction to Vellowind Advisory with a strong visual impact.
- About Us: A brief overview of who we are and our mission.
- Team: Section for the profiles of the two principals.
- Services: A clear and concise presentation of our services, including franchise development, due diligence, and construction management.
- Contact Information: Easy-to-find contact details, including a form for inquiries.
- Call to Action: Encouraging visitors to get in touch with us for consultations or further information.

Design Considerations:
- Ensure the design is responsive and mobile-friendly.
- Include high-quality images and icons that complement our services and industry.
- We do not need development services, this is only a design project.

```html
<!DOCTYPE html>
<html lang="en">
<head>
<meta charset="utf-8">
<title>Vellowind Advisory</title>
<link href="https://fonts.googleapis.com/css2?family=Poppins:wght@300;400;500;600;700&display=swap" rel="stylesheet">
<style>
:root{
  --backdrop:#cfcfcf;
  --white:#ffffff;
  --mint:#eaf5f0;
  --green:#95cbb3;
  --green-deep:#6fb693;
  --green-line:#8ecab0;
  --ink:#3a3a3a;
  --muted:#8a8f8c;
  --field:#ececec;
  --card:#f3f3f3;
}
*{margin:0;padding:0;box-sizing:border-box}
html,body{width:1200px;height:4162px;overflow:hidden}
body{background:var(--backdrop);font-family:'Poppins',sans-serif;color:var(--ink);position:relative}
.page{position:absolute;left:134px;top:121px;width:932px;height:3917px;background:var(--white);overflow:hidden}
section{position:absolute;left:0;width:932px}
.abs{position:absolute}
.brand{font-weight:600;color:var(--green-deep);display:flex;align-items:center;gap:8px}
.brand .dot{width:34px;height:34px;border:3px solid var(--green-line);border-radius:50%}
.eyebrow{font-size:10px;letter-spacing:4px;color:var(--ink)}
.title{font-size:21px;font-weight:400;color:var(--green-deep)}
.copy{font-size:10px;line-height:12.5px;color:var(--muted);font-weight:300}
.btn{background:var(--green);color:var(--white);font-size:8px;text-align:center;border-radius:2px;height:19px;line-height:19px}

/* hero */
.hero{top:0;height:622px}
.hero .brand{left:79px;top:36px;font-size:15px;line-height:14px}
.nav{left:254px;top:47px;display:flex;gap:0;font-size:9px}
.nav span{position:absolute;white-space:nowrap}
.nav-divider{left:229px;top:30px;width:1px;height:46px;background:#ddd}
.hero h1{left:79px;top:205px;font-size:21px;line-height:27px;font-weight:700;color:var(--green-deep)}
.hero .sub{left:79px;top:273px;font-size:9px;font-weight:700;color:var(--ink)}
.hero .copy{left:79px;top:332px;width:290px}
.hero .btn{left:79px;top:487px;width:86px}
.hero-visual{left:420px;top:-30px}

/* about */
.about{top:622px;height:511px;background:var(--mint);overflow:visible}
.about-frame{left:118px;top:37px;width:321px;height:569px;border:2px solid var(--green-line);border-radius:10px}
.about-photo{left:79px;top:68px;width:323px;height:506px;border-radius:10px;background:linear-gradient(160deg,#3f5468,#a9b8c6 55%,#dfe7ee)}
.about .eyebrow{left:486px;top:62px}
.about .title{left:486px;top:80px}
.about .copy{left:486px;top:138px;width:362px}
.about .copy p{margin-bottom:12px}

/* team */
.team{top:1133px;height:641px;background:linear-gradient(180deg,#fff 55%,#eef1f2)}
.team .eyebrow{left:79px;top:176px}
.team .title{left:79px;top:194px}
.team .copy{left:79px;top:303px;width:283px}
.member-photo{left:410px;width:152px;height:184px;border-radius:8px;background:linear-gradient(180deg,#8fa6bd,#c9d3dc)}
.member-card{left:575px;width:357px;height:184px;background:var(--card);border-radius:10px 0 0 10px;padding:16px 30px}
.member-card h3{font-size:12px;font-weight:500}
.member-card .role{font-size:8px;color:var(--green-deep);margin:6px 0 12px}
.member-card p{font-size:5.5px;line-height:7px;color:var(--muted);margin-bottom:6px;width:240px}
.member-card .icons{position:absolute;left:32px;bottom:-8px;display:flex;gap:10px}
.member-card .icons span{width:19px;height:19px;border-radius:50%;background:var(--green)}

/* services */
.services{top:1774px;height:622px;background:var(--green);color:var(--white)}
.svc-circle{border-radius:50%;border:5px solid #f2faf6;background:#a9d5c1;display:flex;flex-direction:column;align-items:center;justify-content:center;text-align:center;padding:0 20px}
.svc-circle h4{font-size:7px;font-weight:600}
.svc-circle p{font-size:5px;line-height:6.5px;margin-top:4px}
.svc-circle.active h4{font-size:10px}
.services .eyebrow{left:452px;top:72px;color:var(--white)}
.services .label{left:452px;top:88px;font-size:19px}
.services .rule{left:452px;top:147px;width:480px;height:1px;background:#dff0e8}
.services h2{left:452px;top:231px;font-size:19px;font-weight:400}
.services .copy{left:452px;top:318px;width:400px;color:var(--white)}
.services .copy p{margin-bottom:12px}

/* contact */
.contact{top:2396px;height:633px}
.contact .eyebrow{left:79px;top:57px;letter-spacing:0;font-size:9px}
.contact .title{left:79px;top:70px}
.contact-frame{left:378px;top:63px;width:473px;height:488px;border:2px solid var(--green-line);border-left:none}
.contact-frame-tick{left:378px;top:63px;width:2px;height:60px;background:var(--green-line)}
.contact-frame-tick.low{top:491px}
.map{left:488px;top:98px;width:331px;height:417px;background:linear-gradient(135deg,#eceff2,#f6efe0 55%,#e6eaee)}
.field{background:var(--field);height:23px;font-size:8px;color:#aaa;padding:6px 8px}
.contact .btn{left:79px;top:540px;width:86px}

/* cta */
.cta{top:3029px;height:392px;background:var(--mint)}
.cta-photo{left:0;top:64px;width:397px;height:245px;background:linear-gradient(180deg,#b9d3ea 0%,#e4ecf1 45%,#8ea0ad 75%,#5f7a58)}
.cta .eyebrow{left:481px;top:64px;letter-spacing:1px;font-size:9px}
.cta .title{left:481px;top:84px;font-size:23px}
.cta .copy{left:481px;top:156px;width:340px}
.cta .btn{left:481px;top:301px;width:110px}

/* touch */
.touch{top:3421px;height:281px;text-align:center}
.touch .brand{left:0;width:932px;top:20px;justify-content:center;font-size:15px}
.touch .small{left:0;width:932px;top:110px;font-size:10px}
.touch .title{left:0;width:932px;top:130px}
.email-bar{left:197px;top:182px;width:533px;height:42px;background:#e2e2e2;border-radius:2px;font-size:10px;letter-spacing:7px;color:#666;text-align:left;padding:13px 30px}
.email-bar svg{position:absolute;right:18px;top:10px}

/* footer */
.footer{top:3702px;height:215px;background:var(--green);color:var(--white)}
.footer .brand{left:79px;top:38px;color:var(--white);font-size:18px}
.footer .brand .dot{border-color:var(--white);width:44px;height:44px}
.footer .legal{left:79px;top:129px;font-size:8px;line-height:15px}
.foot-col{font-size:7px;line-height:10px}
.foot-col h5{font-size:8px;font-weight:600;margin-bottom:10px}
.social{display:flex;gap:4px}
.social span{width:11px;height:11px;border-radius:50%;background:#2d2d2d}
</style>
</head>
<body>
<div class="page">

  <section class="hero">
    <div class="abs brand"><span class="dot"></span><span>Vellowind<br><span style="font-weight:300">Advisory</span></span></div>
    <div class="abs nav-divider"></div>
    <nav class="abs nav" style="left:0;top:47px">
      <span style="left:254px">About</span>
      <span style="left:331px">Services</span>
      <span style="left:426px">Team</span>
      <span style="left:494px">Contact</span>
    </nav>
    <svg class="abs hero-visual" width="560" height="660" viewBox="0 0 560 660" role="img" aria-label="Photo of a hand stacking wooden blocks with shop icons into a pyramid">
      <defs>
        <linearGradient id="wood" x1="0" y1="0" x2="1" y2="1">
          <stop offset="0" stop-color="#9fb5cf"/><stop offset=".4" stop-color="#e3c289"/><stop offset="1" stop-color="#c99a5a"/>
        </linearGradient>
      </defs>
      <rect x="110" y="110" width="420" height="420" rx="90" transform="rotate(45 320 320)" fill="url(#wood)" stroke="#8ecab0" stroke-width="12"/>
    </svg>
    <h1 class="abs">BUILDING SUCCESS<br>IN SOUTHERN CALIFORNIA</h1>
    <p class="abs sub">EXPERTISE AT EVERY STEP: FROM PLANNING TO EXECUTION</p>
    <p class="abs copy">At Vellowind, we blend innovative strategies with local market expertise to guide your commercial real estate ventures. Whether you're launching a new restaurant, investing in retail spaces, or expanding a franchise, our dedicated team is here to turn your real estate aspirations into tangible success. Dive into a partnership that grows with you.</p>
    <div class="abs btn">learn more</div>
  </section>

  <section class="about">
    <div class="abs about-frame"></div>
    <div class="abs about-photo" role="img" aria-label="Photo looking up at glass office towers"></div>
    <p class="abs eyebrow">about us</p>
    <h2 class="abs title">Vellowind Advisory</h2>
    <div class="abs copy">
      <p>Welcome to Vellowind Advisory, your trusted partner in navigating the complexities of the real estate and small business markets. Founded by industry veterans Rafael Moreno and Kevin Tanaka, we specialize in providing comprehensive services tailored to the unique needs of our clients. Whether you're a franchisee, a new restaurant owner, or a commercial real estate investor, our expertise in due diligence, construction management, and investment property evaluation ensures you make informed, strategic decisions.</p>
      <p>At Vellowind Advisory, we are committed to your success. Our approach combines meticulous analysis, strategic insights, and personalized service to help you achieve your business goals. We pride ourselves on our ability to deliver results that exceed expectations, fostering long-term relationships built on trust and excellence.</p>
      <p>Discover how Vellowind Advisory can support your business journey. Partner with us and experience the difference our dedication and expertise can make.</p>
    </div>
  </section>

  <section class="team">
    <p class="abs eyebrow">Our</p>
    <h2 class="abs title">Leadership Team</h2>
    <p class="abs copy">Lorem Ipsum is simply dummy text of the printing and typesetting industry. Lorem Ipsum has been the industry's standard dummy text ever since the 1500s, when an unknown printer took a galley of type and scrambled it to make a type specimen book. It has survived not only five.</p>

    <div class="abs member-photo" style="top:156px" role="img" aria-label="Portrait of Rafael Moreno"></div>
    <article class="abs member-card" style="top:156px">
      <h3>Rafael Moreno</h3>
      <p class="role">Principal</p>
      <p>Rafael brings over 20 years of experience in commercial real estate and franchise strategy across Southern California, guiding owners from site search through opening day.</p>
      <p>His hands-on leadership and market knowledge help clients secure strong locations and lasting returns.</p>
      <div class="icons"><span></span><span></span></div>
    </article>

    <div class="abs member-photo" style="top:390px" role="img" aria-label="Portrait of Kevin Tanaka"></div>
    <article class="abs member-card" style="top:390px">
      <h3>Kevin Tanaka</h3>
      <p class="role">Principal</p>
      <p>Kevin is a seasoned real estate advisor with deep experience in construction management and retail leasing for growing brands.</p>
      <p>His network of industry partners and focus on detail help clients build value and scale with confidence.</p>
      <div class="icons"><span></span><span></span></div>
    </article>
  </section>

  <section class="services">
    <svg class="abs" style="left:203px;top:28px" width="20" height="12" viewBox="0 0 20 12"><path d="M2 10 L10 2 L18 10" fill="none" stroke="#fff" stroke-width="1.5"/></svg>
    <div class="abs svc-circle" style="left:152px;top:73px;width:122px;height:122px">
      <h4>Franchise development</h4><p>Turning proven concepts into scalable franchise systems</p>
    </div>
    <div class="abs svc-circle active" style="left:119px;top:214px;width:188px;height:188px">
      <h4>construction management</h4><p>Conducting thorough due diligence for business and property transactions to identify potential risks and liabilities</p>
    </div>
    <div class="abs svc-circle" style="left:152px;top:419px;width:122px;height:122px">
      <h4>due diligence</h4><p>Comprehensive review of sites and deals for informed investment</p>
    </div>
    <svg class="abs" style="left:203px;top:576px" width="20" height="12" viewBox="0 0 20 12"><path d="M2 2 L10 10 L18 2" fill="none" stroke="#fff" stroke-width="1.5"/></svg>

    <p class="abs eyebrow">Our</p>
    <p class="abs label">services</p>
    <div class="abs rule"></div>
    <h2 class="abs">Franchise Development &amp; Launch</h2>
    <div class="abs copy">
      <p>At Vellowind Advisory, our Franchise Development &amp; Launch service is designed to transform your successful business into a thriving franchise. We start by thoroughly evaluating your business model to determine its franchisability. Once confirmed, our team handles every aspect of the franchise setup, including legal documentation, branding, marketing strategies, operational guidelines, and franchisee recruitment.</p>
      <p>Our goal is to ensure a seamless and efficient transition from a single successful location to a robust franchise network, empowering your business to scale effectively and achieve exponential growth. Partner with us to turn your business into a nationwide brand.</p>
    </div>
  </section>

  <section class="contact">
    <p class="abs eyebrow">Leave us a</p>
    <h2 class="abs title">massage</h2>
    <div class="abs contact-frame"></div>
    <div class="abs contact-frame-tick"></div>
    <div class="abs contact-frame-tick low"></div>
    <div class="abs map" role="img" aria-label="Street map showing the office location"></div>
    <form>
      <div class="abs field" style="left:79px;top:195px;width:183px">Name</div>
      <div class="abs field" style="left:275px;top:195px;width:182px">Last Name</div>
      <div class="abs field" style="left:79px;top:232px;width:378px">company</div>
      <div class="abs field" style="left:79px;top:269px;width:183px">phone</div>
      <div class="abs field" style="left:275px;top:269px;width:182px">email</div>
      <div class="abs field" style="left:79px;top:296px;width:378px;height:180px">Additional Information</div>
      <div class="abs btn">Submit</div>
    </form>
  </section>

  <section class="cta">
    <div class="abs cta-photo" role="img" aria-label="Photo of modern office buildings behind a green lawn"></div>
    <p class="abs eyebrow">Unlock Your Business</p>
    <h2 class="abs title">Potential Today!</h2>
    <p class="abs copy">At Vellowind Advisory, we're dedicated to turning your business aspirations into reality. Our expertise and commitment ensure you make informed, strategic decisions that drive success. Take the first step towards achieving your goals with confidence.</p>
    <div class="abs btn">Get started now</div>
  </section>

  <section class="touch">
    <div class="abs brand"><span class="dot"></span><span>Vellowind Advisory</span></div>
    <p class="abs small">get in touch with us for</p>
    <h2 class="abs title">consultations or further information.</h2>
    <div class="abs email-bar">email address
      <svg width="24" height="22" viewBox="0 0 24 22"><path d="M1 10 L23 1 L17 21 L11 13 Z M11 13 L23 1" fill="none" stroke="#777" stroke-width="1.6" stroke-linejoin="round"/></svg>
    </div>
  </section>

  <footer class="abs footer" style="left:0;width:932px">
    <div class="abs brand"><span class="dot"></span><span>Vellowind<br>Advisory</span></div>
    <p class="abs legal">Copyright2024Vellowind Advisory All Right Rendered<br>Privacy policy | Term and condition</p>
    <div class="abs foot-col" style="left:410px;top:45px;width:140px">
      <h5>CONTACT US</h5>
      <p>Lorem Ipsum is simply dummy text of the printing and typesetting industry. Lorem Ipsum has been the industry's</p>
    </div>
    <div class="abs foot-col" style="left:609px;top:45px">
      <h5>NAVIGATE</h5>
      <p>About us<br>Services<br>Team<br>contact us</p>
    </div>
    <div class="abs foot-col" style="left:770px;top:45px">
      <h5>FOLLOW US</h5>
      <div class="social"><span></span><span></span></div>
    </div>
  </footer>

</div>
</body>
</html>
```